Business Card Project

We are a small consulting firm. You can experiment with any design.
Must have:
1) Company name - OLUNDEX International
2) Company slogan - simple solutions for complex problems
3) Name/Title/Phone/Email/WWW/ - use anything you like as an example.

Industry/Entity Type

Business

```html
<!DOCTYPE html>
<html lang="en">
<head>
<meta charset="utf-8">
<title>OLUNDEX International – Business Cards</title>
<link rel="stylesheet" href="https://fonts.googleapis.com/css2?family=Arimo:wght@400&family=Questrial&display=swap">
<style>
  :root {
    --backdrop: #b46a34;
    --card-dark: #1d1f24;
    --card-light: #ffffff;
    --accent-blue: #2a9de0;
    --text-light: #e6e8eb;
    --text-muted: #8c8f94;
    --tagline-grey: #9a9a9a;
    --brand-grey: #4a4d52;
  }
  * { margin: 0; padding: 0; box-sizing: border-box; }
  html, body {
    width: 1200px;
    height: 684px;
    overflow: hidden;
    background: var(--backdrop);
  }
  .canvas {
    position: relative;
    width: 1200px;
    height: 684px;
  }
  .card {
    position: absolute;
    overflow: hidden;
    box-shadow: 0 2px 6px rgba(0,0,0,0.35);
  }

  .brand {
    position: absolute;
    display: flex;
    align-items: center;
  }
  .brand__dot {
    border-radius: 50%;
    background: var(--accent-blue);
    flex: none;
  }
  .brand__name {
    font-family: "Questrial", sans-serif;
    letter-spacing: 0.04em;
    white-space: nowrap;
  }
  .tagline {
    position: absolute;
    font-family: "Arimo", sans-serif;
    white-space: nowrap;
  }

  /* Front card */
  .card--front {
    left: 160px; top: 144px;
    width: 420px; height: 256px;
    background: var(--card-dark);
  }
  .card--front .brand { left: 60px; top: 82px; }
  .card--front .brand__dot { width: 46px; height: 46px; margin-right: 12px; }
  .card--front .brand__name { font-size: 17px; color: var(--text-light); }
  .card--front .tagline {
    left: 64px; top: 146px;
    font-size: 14px;
    color: var(--text-muted);
  }

  /* Back card */
  .card--back {
    left: 628px; top: 296px;
    width: 421px; height: 257px;
    background: var(--card-light);
  }
  .card--back .brand { left: 23px; top: 36px; }
  .card--back .brand__dot { width: 36px; height: 36px; margin-right: 10px; }
  .card--back .brand__name { font-size: 13px; color: var(--brand-grey); }
  .card--back .tagline {
    left: 25px; top: 86px;
    font-size: 11px;
    color: var(--tagline-grey);
  }
  .card__rule {
    position: absolute;
    left: 0; top: 134px;
    width: 100%; height: 3px;
    background: var(--accent-blue);
  }
  .card__footer {
    position: absolute;
    left: 0; top: 140px;
    width: 100%; height: 117px;
    background: var(--card-dark);
    font-family: "Arimo", sans-serif;
  }
  .person {
    position: absolute;
    left: 27px; top: 38px;
  }
  .person__name {
    font-size: 16px;
    color: var(--accent-blue);
    letter-spacing: 0.02em;
  }
  .person__title {
    margin-top: 4px;
    font-size: 9px;
    color: var(--text-muted);
  }
  .contacts {
    position: absolute;
    left: 248px; top: 20px;
    list-style: none;
  }
  .contacts li {
    display: flex;
    align-items: center;
    height: 21.3px;
    font-size: 11px;
    color: var(--text-light);
    white-space: nowrap;
  }
  .contacts li::before {
    content: "";
    width: 4px; height: 4px;
    border-radius: 50%;
    background: var(--accent-blue);
    margin-right: 8px;
  }
</style>
</head>
<body>
<main class="canvas">
  <section class="card card--front" aria-label="Business card front">
    <div class="brand">
      <span class="brand__dot"></span>
      <span class="brand__name">OLUNDEX INTERNATIONAL</span>
    </div>
    <p class="tagline">Simple Solutions For Complex Problems</p>
  </section>

  <section class="card card--back" aria-label="Business card back">
    <div class="brand">
      <span class="brand__dot"></span>
      <span class="brand__name">OLUNDEX INTERNATIONAL</span>
    </div>
    <p class="tagline">Simple Solutions For Complex Problems</p>
    <div class="card__rule"></div>
    <div class="card__footer">
      <div class="person">
        <p class="person__name">MARCUS HALE</p>
        <p class="person__title">Creative Director</p>
      </div>
      <ul class="contacts">
        <li>88 Harbor Lane Suite 4</li>
        <li>hello@olundex.com</li>
        <li>0142 587 903</li>
        <li>www.olundex.com</li>
      </ul>
    </div>
  </section>
</main>
</body>
</html>
```